I would like a formal monogram with MR and Marlena Rosk Interiors written somehow. this a a new interior design company based in Dallas. My favorite colors is Halvorn blue with gold or white writing or some variation of.
back: Marlena Rosk
214-555-0163
marlena.rosk@fernmail.example
www.marlenaroskinteriors.example

```html
<!DOCTYPE html>
<html lang="en">
<head>
<meta charset="utf-8">
<title>Marlena Rosk Interiors — Business Card</title>
<link rel="stylesheet" href="https://fonts.googleapis.com/css2?family=Cinzel:wght@400&family=Montserrat:wght@300;400&family=Roboto:wght@300&display=swap">
<style>
  :root {
    --backdrop: #2a2a2a;
    --card: #efefef;
    --card-shade: #e3e3e3;
    --teal: #14a398;
    --teal-deep: #0c948a;
    --gold-dark: #8a6120;
    --gold: #c79a3e;
    --gold-light: #e6c05a;
    --ink: #3d3d3d;
  }
  * { margin: 0; padding: 0; box-sizing: border-box; }
  html, body {
    width: 1200px; height: 1138px; overflow: hidden;
    background: var(--backdrop);
  }
  .card {
    position: absolute;
    width: 620px; height: 375px;
    border-radius: 16px;
    overflow: hidden;
    background: linear-gradient(180deg, var(--card) 0%, #ececec 60%, var(--card-shade) 100%);
  }
  .card--front { left: 272px; top: 184px; }
  .card--back  { left: 274px; top: 606px; }

  /* Front */
  .front-mark {
    position: absolute; left: 0; right: 0; top: 84px;
    display: flex; justify-content: center; align-items: center; gap: 12px;
  }
  .mark-dot {
    width: 14px; height: 14px; border-radius: 50%;
    background: var(--gold);
  }
  .mark-letters {
    font-family: "Cinzel", serif; font-weight: 400;
    font-size: 62px; line-height: 1; color: var(--teal);
  }
  .wordmark {
    position: absolute; left: 0; right: 0; text-align: center;
  }
  .front-name {
    top: 190px;
    font-family: "Cinzel", serif; font-weight: 400;
    font-size: 46px; line-height: 1; color: var(--teal);
  }
  .front-tagline {
    top: 244px;
    font-family: "Montserrat", sans-serif; font-weight: 400;
    font-size: 21px; letter-spacing: 27px; padding-left: 27px;
    color: var(--ink); line-height: 1;
  }
  .front-web {
    position: absolute; left: 0; right: 0; top: 332px;
    display: flex; justify-content: center; align-items: center; gap: 14px;
    font-family: "Roboto", sans-serif; font-weight: 300;
    font-size: 16px; color: var(--ink);
  }
  .rule {
    width: 82px; height: 2px;
    background: linear-gradient(90deg, var(--gold-dark), var(--gold-light), var(--gold-dark));
  }
  .edge-band {
    position: absolute; left: 0; right: 0; bottom: 0; height: 12px;
    display: flex;
  }
  .edge-band__teal { flex: 1; background: var(--teal-deep); }
  .edge-band__gold {
    flex: 1;
    background: linear-gradient(90deg, var(--gold-dark), var(--gold-light) 45%, var(--gold-dark) 85%, var(--gold));
  }

  /* Back */
  .back-name {
    position: absolute; left: 24px; top: 100px;
    font-family: "Cinzel", serif; font-weight: 400;
    font-size: 30px; line-height: 1; color: var(--teal);
  }
  .back-tagline {
    position: absolute; left: 34px; top: 136px;
    font-family: "Montserrat", sans-serif; font-weight: 300;
    font-size: 13px; letter-spacing: 19.5px;
    color: var(--ink); line-height: 1;
  }
  .person {
    position: absolute; left: 26px; top: 202px;
    font-family: "Cinzel", serif; font-weight: 400;
    font-size: 24px; line-height: 1; color: var(--teal);
  }
  .contacts {
    position: absolute; left: 26px; top: 266px;
    list-style: none;
    font-family: "Roboto", sans-serif; font-weight: 300;
    font-size: 16px; color: var(--ink);
  }
  .contacts li {
    display: flex; align-items: center; gap: 15px;
    height: 24px;
  }
  .contacts svg { width: 16px; height: 16px; fill: var(--teal); flex: none; }
  .back-mark {
    position: absolute; left: 380px; top: 78px;
    width: 260px; height: 250px;
  }
  .back-mark__ring {
    position: absolute; left: 0; top: 0;
    width: 240px; height: 240px; border-radius: 50%;
    border: 10px solid var(--teal);
  }
  .back-mark__letters {
    position: absolute; left: 0; top: 0; width: 240px; height: 240px;
    display: flex; align-items: center; justify-content: center;
    font-family: "Cinzel", serif; font-weight: 400;
    font-size: 104px; line-height: 1; color: var(--teal);
  }
</style>
</head>
<body>

<section class="card card--front" aria-label="Business card front">
  <div class="front-mark">
    <span class="mark-dot"></span>
    <span class="mark-letters">MR</span>
  </div>
  <h1 class="wordmark front-name">MARLENA ROSK</h1>
  <p class="wordmark front-tagline">INTERIORS</p>
  <div class="front-web">
    <span class="rule"></span>
    <span>www.marlenaroskinteriors.example</span>
    <span class="rule"></span>
  </div>
  <div class="edge-band">
    <span class="edge-band__teal"></span>
    <span class="edge-band__gold"></span>
  </div>
</section>

<section class="card card--back" aria-label="Business card back">
  <h2 class="back-name">MARLENA ROSK</h2>
  <p class="back-tagline">INTERIORS</p>
  <p class="person">MARLENA ROSK</p>
  <ul class="contacts">
    <li>
      <svg viewBox="0 0 16 16" aria-hidden="true"><path d="M1 6c0-2 3-3.5 7-3.5S15 4 15 6v1.5h-3.5V6c-1-.6-2.2-.8-3.5-.8S5.5 5.4 4.5 6v1.5H1z"/><path d="M3.5 8.5h9L14 14H2z"/></svg>
      <span>214-555-0163</span>
    </li>
    <li>
      <svg viewBox="0 0 16 16" aria-hidden="true"><path d="M1 3h14v10H1z" fill="none" stroke="#14a398" stroke-width="1.6"/><path d="M1 3l7 6 7-6" fill="none" stroke="#14a398" stroke-width="1.6"/></svg>
      <span>marlena.rosk@fernmail.example</span>
    </li>
    <li>
      <svg viewBox="0 0 16 16" aria-hidden="true"><g fill="none" stroke="#14a398" stroke-width="1.3"><circle cx="8" cy="8" r="6.5"/><ellipse cx="8" cy="8" rx="3" ry="6.5"/><path d="M1.5 8h13M2.5 4.8h11M2.5 11.2h11"/></g></svg>
      <span>www.marlenaroskinteriors.example</span>
    </li>
  </ul>
  <div class="back-mark">
    <span class="back-mark__ring"></span>
    <span class="back-mark__letters">MR</span>
  </div>
</section>

</body>
</html>
```